IT Freelancer (Consulting, trainer and project manager) needed letterhead

As a freelancer for IT Trainingswhip, consulting and project management I need a letterhead design. What is desired is a design that fits the existing logo (see Annex). It is functional, reliable, and equal time wirkenn Agil and modern. The whole is in color, as well as printed out to make a good impression on a black and white printer. The whole is to the existing Cooperate design (business card, homepage, logo) fit. Therefore, the choice of colors.
Updates

Target Market(s)

Customers such as medium-sized enterprises, training institutions

Industry/Entity Type

Consulting

Colors
0455a3
3277b5
85abd2
cfdfed
34a6d7
32a6d6
249fd4
0792cd
85cae6

Requirements
Must have
• Must include logo (see Annex) address (Brennerweg 14, 95652 Waldsassen, Germany). Must seriously and act simultaneously Agil. Design should (even) be adaptable (signature, address, etc.) design must look good on a black / white laser

```html
<!DOCTYPE html>
<html lang="de">
<head>
<meta charset="utf-8">
<title>Konrad Albers – Briefbogen</title>
<link rel="stylesheet" href="https://fonts.googleapis.com/css2?family=Montserrat:wght@500;700&display=swap">
<style>
  :root {
    --navy: #0455a3;
    --blue: #3277b5;
    --sky: #249fd4;
    --sky-light: #34a6d7;
    --mist: #85cae6;
    --paper: #ffffff;
    --watermark: #ececec;
    --text-grey: #6b6b6b;
  }
  * { margin: 0; padding: 0; box-sizing: border-box; }
  html, body { width: 800px; height: 1200px; overflow: hidden; background: var(--paper); }
  .letterhead {
    position: relative;
    width: 800px;
    height: 1200px;
    background: var(--paper);
    font-family: "Montserrat", sans-serif;
  }
  .letterhead__waves { position: absolute; inset: 0; width: 800px; height: 1200px; }
  .brand {
    position: absolute;
    top: 40px;
    left: 50%;
    transform: translateX(-50%);
    display: flex;
    align-items: center;
    gap: 12px;
  }
  .brand__dot {
    width: 62px; height: 62px;
    border-radius: 50%;
    background: var(--navy);
  }
  .brand__name {
    color: var(--navy);
    font-weight: 700;
    font-size: 22px;
    line-height: 1.05;
    letter-spacing: 0.06em;
    text-transform: uppercase;
  }
  .watermark {
    position: absolute;
    left: 400px; top: 600px;
    width: 570px; height: 570px;
    margin: -285px 0 0 -285px;
    border-radius: 50%;
    border: 28px solid var(--watermark);
  }
  .sender-address {
    position: absolute;
    top: 1140px;
    left: 0; right: 0;
    text-align: center;
    font-size: 13px;
    font-weight: 500;
    letter-spacing: 0.04em;
    text-transform: uppercase;
    color: var(--text-grey);
  }
</style>
</head>
<body>
<main class="letterhead">
  <svg class="letterhead__waves" viewBox="0 0 800 1200" aria-hidden="true">
    <path d="M0 70 Q400 200 800 55 L800 62 Q400 190 0 78 Z" fill="var(--sky-light)"/>
    <path d="M0 90 Q400 205 800 75 L800 90 Q400 225 0 104 Z" fill="var(--navy)"/>
    <path d="M0 104 Q400 225 800 90 L800 96 Q400 232 0 110 Z" fill="var(--mist)"/>
    <path d="M0 1085 Q380 1010 800 1100 L800 1108 Q380 1022 0 1094 Z" fill="var(--sky)"/>
    <path d="M0 1098 Q380 1030 800 1116 L800 1134 Q380 1045 0 1112 Z" fill="var(--navy)"/>
    <path d="M0 1112 Q380 1045 800 1134 L800 1140 Q380 1054 0 1118 Z" fill="var(--mist)"/>
  </svg>

  <header class="brand">
    <span class="brand__dot"></span>
    <span class="brand__name">Konrad<br>Albers</span>
  </header>

  <div class="watermark" role="img" aria-label="Faint brand emblem watermark"></div>

  <footer class="sender-address">Brennerweg 14, 92637 Lindenau, Germany</footer>
</main>
</body>
</html>
```